Bright Meadow Dental - Stationary
Business Cards, Letterhead, & Envelope
Project: Bright Meadow Dental - Stationary
Bright Meadow Dental - Stationary - Health
Creative Brief
Professional
Leland Fisk, D.D.S.
3847 W Thornbury Ln, Suite 2 Gladstone, MO 64102
BrightMeadowDental@mailbox-example.com
www.BrightMeadowDental-example.com
We're a fun office and want people to expect great cosmetic work and accommodations for families. We don't need a "blow your mind" presentation, just something classy.

```html
<!DOCTYPE html>
<html lang="en">
<head>
<meta charset="utf-8">
<title>Bright Meadow Dental – Stationery</title>
<link rel="stylesheet" href="https://fonts.googleapis.com/css2?family=Cinzel:wght@500&family=Open+Sans:wght@400;600&display=swap">
<style>
  :root{
    --stage:#9d9d9d;
    --paper:#ffffff;
    --blue:#1f5fb4;
    --blue-deep:#123f8c;
    --blue-light:#4f97e0;
    --ink:#3a3a3a;
  }
  *{margin:0;padding:0;box-sizing:border-box}
  html,body{width:1200px;height:684px;overflow:hidden}
  body{background:var(--stage);font-family:"Open Sans",Arial,sans-serif;color:var(--ink);position:relative}
  .sheet{position:absolute;background:var(--paper);box-shadow:0 1px 3px rgba(0,0,0,.25);overflow:hidden}

  .brand{position:absolute;color:var(--blue);font-family:"Cinzel",Georgia,serif;font-weight:500;line-height:1.05;letter-spacing:.5px;white-space:nowrap}
  .brand .tag{display:block;font-family:"Open Sans",Arial,sans-serif;font-weight:600;letter-spacing:0;color:var(--blue)}

  /* business card */
  .card{left:24px;top:281px;width:152px;height:91px}
  .card .band{position:absolute;left:0;top:0;width:100%;height:27px;background:linear-gradient(90deg,var(--paper) 35%,var(--blue-light) 70%,var(--blue) 100%)}
  .card .brand{left:6px;top:5px;font-size:9px}
  .card .brand .tag{font-size:3.8px;margin-top:3px}
  .card .details{position:absolute;left:7px;top:44px;font-size:4px;line-height:5.8px}
  .card .person{position:absolute;right:8px;top:57px;font-size:4.5px}
  .card .footer{position:absolute;left:0;bottom:0;width:100%;height:9px;background:var(--blue);color:#fff;font-size:4px;line-height:9px;padding-left:7px}

  /* letterhead */
  .letterhead{left:187px;top:5px;width:430px;height:672px}
  .letterhead .band{position:absolute;left:0;top:0;width:100%;height:62px;background:linear-gradient(90deg,var(--paper) 25%,var(--blue-light) 65%,var(--blue) 100%)}
  .letterhead .brand{left:16px;top:14px;font-size:22px}
  .letterhead .brand .tag{font-size:7px;margin-top:4px}
  .letterhead .rule{position:absolute;left:0;width:100%;height:2px;background:var(--blue)}
  .letterhead .contact{position:absolute;left:14px;top:638px;font-size:5.2px;white-space:nowrap}
  .letterhead .footer{position:absolute;left:0;bottom:0;width:100%;height:18px;background:linear-gradient(90deg,var(--blue-deep),var(--blue-light));color:#fff;font-size:5.5px;line-height:18px;padding-left:14px}

  /* envelope back */
  .envelope-back{left:643px;top:36px;width:547px;height:276px}
  .envelope-back .flap{position:absolute;left:0;top:0}
  .envelope-back .seal{position:absolute;left:233px;top:18px;width:80px;text-align:center;color:#fff;font-family:"Cinzel",Georgia,serif;font-weight:500;font-size:9px;line-height:1.2}

  /* envelope front */
  .envelope-front{left:643px;top:372px;width:547px;height:300px}
  .envelope-front .band{position:absolute;left:0;top:0;width:100%;height:52px;background:linear-gradient(90deg,var(--paper) 25%,var(--blue-light) 65%,var(--blue) 100%)}
  .envelope-front .brand{left:16px;top:14px;font-size:20px}
  .envelope-front .brand .tag{font-size:6.5px;margin-top:4px}
  .envelope-front .rule{position:absolute;left:0;width:100%;height:2px;background:var(--blue)}
  .envelope-front .contact{position:absolute;left:14px;top:267px;font-size:5.2px;white-space:nowrap}
  .envelope-front .footer{position:absolute;left:0;bottom:0;width:100%;height:14px;background:linear-gradient(90deg,var(--blue-deep),var(--blue-light));color:#fff;font-size:5.5px;line-height:14px;padding-left:14px}
</style>
</head>
<body>

<section class="sheet card">
  <div class="band"></div>
  <div class="brand">BRIGHT MEADOW<br>DENTAL<span class="tag">Cosmetic and Family Dentistry</span></div>
  <div class="details">P 620-555-0142<br>F 620-555-0143<br>3847 W Thornbury Ln, Suite 2<br>Fairhaven, KS 67301</div>
  <div class="person">Leland Fisk, D.D.S.</div>
  <div class="footer">lfisk@mailbox-example.com</div>
</section>

<section class="sheet letterhead">
  <div class="band"></div>
  <div class="brand">BRIGHT MEADOW<br>DENTAL<span class="tag">Cosmetic and Family Dentistry</span></div>
  <div class="rule" style="top:630px"></div>
  <div class="contact">P 620-555-0142 &nbsp;|&nbsp; F 620-555-0143 &nbsp;|&nbsp; BrightMeadowDental@mailbox-example.com &nbsp;|&nbsp; 3847 W Thornbury Ln, Suite 2 Fairhaven, KS 67301</div>
  <div class="footer">www.BrightMeadowDental-example.com</div>
</section>

<section class="sheet envelope-back">
  <svg class="flap" width="547" height="110" viewBox="0 0 547 110">
    <defs>
      <linearGradient id="flapFill" x1="0" y1="0" x2="1" y2="0">
        <stop offset="0" stop-color="#123f8c"/>
        <stop offset=".5" stop-color="#2f7bd0"/>
        <stop offset="1" stop-color="#123f8c"/>
      </linearGradient>
    </defs>
    <path d="M0 0H547V56Q547 70 533 70H300Q273 72 273 100Q273 72 246 70H14Q0 70 0 56Z" fill="url(#flapFill)"/>
  </svg>
  <div class="seal">BRIGHT<br>MEADOW</div>
</section>

<section class="sheet envelope-front">
  <div class="band"></div>
  <div class="brand">BRIGHT MEADOW<br>DENTAL<span class="tag">Cosmetic and Family Dentistry</span></div>
  <div class="rule" style="top:259px"></div>
  <div class="contact">P 620-555-0142 &nbsp;|&nbsp; F 620-555-0143 &nbsp;|&nbsp; BrightMeadowDental@mailbox-example.com &nbsp;|&nbsp; 3847 W Thornbury Ln, Suite 2 Fairhaven, KS 67301</div>
  <div class="footer">www.BrightMeadowDental-example.com</div>
</section>

</body>
</html>
```